KiteSurf Weather App Forecast Screen re-design (1 Screen)

We are redesigning our application, BreezeLedger. Our main screen is the forecast screen. The forecast screen presents the forecast for multiple places for the selected day.

Intro
-----

The user has a list of favorite spots that he is monitoring. Then he selects the date that he wants to get the forecast. The forecast screen presents a list of all the spots and a summary of the weather conditions. Spots are sorted by weather conditions. At the top, he gets the spot with the best weather conditions. We have an algorithm that can evaluate whether given weather conditions are good or not. When they are good we indicate that to the user.

Current Solution
------------------

Our current screen looks like the attachment named: "Current Forecast Screen.jpeg"

There is also a landscape version, which contains a bit more data: "Current Forecast Screen Lanscape.jpeg". The landscape one is a bit funny, as it is taken from an Norvo Q7 and the app was not designed for it at the time.

The bars that you see for each hour use our algorithm to display whether the conditions are good:

- When the color is gray the conditions are not good
- When the color is yellow there are light wind conditions
- When the color is green there are good
- When the color is red the wind is very strong
- The height of the bar indicates wind strength

More Info
-----------

The detailed forecast screen is also attached so you can get a bit more context, "DetailedForecast.jpeg"

An example from an application that has a similar chart is attached, "SimilarApp.jpeg". I have circled the chart with red.

Future Solution
------------------

(See note.jpeg)

We want to create a page that contains more information and passes a better message to our users.

The elements that are important and we want to present to the user are the following:

1. Wind. (The most important)
It contains two elements: strength and direction.

1.1 Wind Strength.
Good wind strength is anything between 10-45 knots (measurement unit like km/h). The best representation with a color palette.
Gray will be the color used when the strength is not between 10-45.
The palette should start with yellow at 10 knots, then move toward green for 22knots and finally go towards red for 45 knots.

1.2 Wind Direction.
There are good wind directions that we can kite and directions that is is not possible.
Can be presented by an arrow that points in the direction the wind is blowing to. The color of the arrow will be green when the direction is good, yellow when it is average and gray when it is not good.

My thought for portrait mode is to use an arrow point for the direction and the color of the arrow to represent the strength. Solution number 2 on my notes. Then for landscape, we could use both a number and an arrow like number 4 on my notes.

2. Wave.
It contains three elements: height, period and direction. It is not displayed to all of our users only the ones that have selected the wave riding option.

2.1 Height is represented by a number. Ex. 1.2 meters or 2 foot.
2.2 Period is represented in seconds. Ex. 12 seconds.
2.3 Directions is an arrow that points to the direction the wave is coming from.

Again the solution should be like the wind. Arrow for direction and the color of the arrow for height. The palette here should be something with different blue colors.

3. Tide height. (Optional for tidal spots, as not all spots have tides)

The best way to represent that it through a graph. I would also like to see an alternative, where we have three symbols for low, mid and high tide.

4. General Weather. Rain/Snow and temperature.

This should be represented by a sun/cloud/rain symbol. If it is very cold the symbol can also contain an ice sign on the background.

---------

This is a guideline creativity will be valued. Maybe there is another way to do it that I have not thought about.

The winner of the competition will have to send us all graphics used in vector format, so we can input them to our xCode project.

Finally the person that wins the competition will be the first one to be considered for the redesign of the rest of our application.

Target Market(s)

Kitesurfers

Font styles to use
Sans Serif

Colors

Designer to choose colors to be used in the design.

Requirements
Must have
• It should be minimal and clearly communicate the weather forecast to my users. It should be user friendly.
Nice to have
• Communicative color palettes for both wind strength, tide and waves
Should not have
• Hard to understand UI

```html
<!DOCTYPE html>
<html lang="en">
<head>
<meta charset="utf-8">
<title>KiteSurf Weather App — Forecast Screen</title>
<link rel="stylesheet" href="https://fonts.googleapis.com/css2?family=Roboto:wght@300;400;500;700;900&display=swap">
<style>
:root{
  --page:#eef3f7;
  --brand:#0a7fd6;
  --ink:#2b2f36;
  --muted:#7b8189;
  --sky-light:#cfe9f8;
  --teal:#5cc9c0;
  --teal-deep:#2f8f95;
  --panel-dark:#34545d;
  --tab:#8fd4f5;
  --bar-gray:#e9ecef;
  --bar-yellow:#f6d70c;
  --bar-green:#5fd6a8;
  --bar-red:#f0325f;
  --chip-green:#5fd6a8;
  --chip-yellow:#f6d70c;
  --chip-red:#f0325f;
  --chip-gray:#d9dcdf;
  --night:#1f2a30;
}
*{box-sizing:border-box;margin:0;padding:0}
html,body{width:1126px;height:1200px;overflow:hidden}
body{background:var(--page);font-family:'Roboto',sans-serif;color:var(--ink);position:relative}

/* ---------- screens ---------- */
.screen{position:absolute;width:270px;height:560px;border-radius:34px;overflow:hidden;box-shadow:0 18px 40px rgba(20,60,90,.18)}
.screen--outlook{left:140px;top:40px;background:linear-gradient(180deg,var(--sky-light),#eaf6fc 70%,#f6fafc)}
.screen--detail{left:460px;top:40px}
.screen--calendar{left:702px;top:616px;width:260px;background:var(--night)}

.status{display:flex;justify-content:space-between;align-items:center;padding:14px 22px 0;font-size:11px;font-weight:500}
.status__signal{display:flex;gap:2px;align-items:flex-end}
.status__signal i{display:block;width:3px;background:currentColor;border-radius:1px}

.topbar{display:flex;align-items:center;justify-content:space-between;padding:12px 16px 8px}
.topbar__title{font-size:12px;font-weight:500;letter-spacing:.5px}
.topbar__actions{display:flex;gap:10px;align-items:center}

/* spot cards */
.spots{padding:0 8px;display:flex;flex-direction:column;gap:6px}
.spot{position:relative;height:78px;border-radius:8px;overflow:hidden;color:#fff}
.spot__photo{position:absolute;inset:0;background:linear-gradient(160deg,#7f97a3,#5c7480 55%,#8aa0a8)}
.spot__info{position:absolute;left:10px;top:8px;width:84px}
.spot__name{font-size:11px;font-weight:500;white-space:nowrap}
.chips{display:flex;gap:3px;margin:4px 0}
.chip{font-size:7px;padding:1px 4px;border-radius:3px;color:#fff}
.chip--live{background:var(--chip-green)}
.chip--good{background:var(--chip-green)}
.chip--light{background:var(--chip-yellow);color:#333}
.chip--strong{background:var(--chip-red)}
.chip--bad{background:var(--chip-gray);color:#333}
.spot__dist{font-size:9px;display:flex;gap:6px;align-items:center}
.chart{position:absolute;right:10px;bottom:6px;display:flex;gap:6px;align-items:flex-end}
.chart__col{display:flex;flex-direction:column;align-items:center;gap:3px;width:12px}
.bar{width:5px;border-radius:2px;background:var(--bar-gray)}
.bar--y{background:var(--bar-yellow)}.bar--g{background:var(--bar-green)}.bar--r{background:var(--bar-red)}
.chart__hour{font-size:7px;opacity:.9}
.chart__label{position:absolute;left:100px;bottom:6px;font-size:6px;opacity:.8}

/* tab bar */
.tabbar{position:absolute;left:0;right:0;bottom:0;height:66px;display:flex;justify-content:space-between;align-items:flex-end;padding:0 24px 10px;background:rgba(255,255,255,.92)}
.tabbar__item{display:flex;flex-direction:column;align-items:center;gap:4px;font-size:8px;font-weight:500}
.tabbar__calendar{position:absolute;left:50%;bottom:0;transform:translateX(-50%);width:56px;height:62px;border-radius:10px 10px 0 0;background:var(--tab);display:flex;align-items:center;justify-content:center}

/* detail */
.detail__hero{position:absolute;inset:0 0 auto 0;height:300px;background:linear-gradient(180deg,#6ad2c6,#4fbcb6 60%,#7fcfc8);color:#fff}
.detail__head{position:relative;color:#fff}
.detail__location{font-size:11px;font-weight:500;letter-spacing:.6px}
.follow{font-size:9px;background:rgba(255,255,255,.35);padding:3px 10px;border-radius:10px}
.avatar{width:22px;height:22px;border-radius:50%;background:#c98e7a}
.detail__spot{position:relative;padding:10px 18px 0;color:#fff}
.detail__spotname{font-size:30px;font-weight:300;display:flex;align-items:flex-start;gap:6px}
.detail__spotname .chip{margin-top:6px}
.detail__stats{display:flex;align-items:flex-end;gap:18px;margin-top:6px}
.detail__temp{font-size:44px;font-weight:300;line-height:1}
.stat{text-align:center}
.stat b{display:block;font-size:15px;font-weight:500}
.stat span{font-size:9px;opacity:.85}
.detail__sub{font-size:10px;margin-top:6px;opacity:.9}
.hourly{position:absolute;left:0;right:0;top:214px;bottom:0;background:linear-gradient(180deg,var(--panel-dark),#3e6870 70%,#6f9aa0);color:#fff;padding:12px 12px 0}
.hour{display:grid;grid-template-columns:54px 24px 34px 1fr 1fr 1fr 30px;align-items:center;height:52px;font-size:10px;border-bottom:1px solid rgba(255,255,255,.08)}
.hour__time b{font-size:12px;font-weight:500}
.hour__time small{font-size:7px}
.cell{display:flex;flex-direction:column;align-items:center;gap:1px}
.cell small{font-size:6px;opacity:.7}
.warn{color:var(--bar-red);font-weight:500;font-size:12px}
.tabbar--clear{background:transparent;color:#fff}

/* calendar */
.calendar__list{padding:0 8px;display:flex;flex-direction:column;gap:8px}
.ghost{height:96px;border-radius:8px;background:#263238;position:relative;opacity:.75}
.ghost .chart{right:8px}
.ghost .bar{opacity:.55}
.picker{position:absolute;left:0;right:0;bottom:76px;background:#fff;padding:12px 8px 6px;border-radius:6px 6px 0 0}
.picker__head{display:flex;justify-content:center;gap:24px;font-size:12px;font-weight:500;margin-bottom:10px}
.picker__days{display:flex;justify-content:space-between}
.day{width:30px;text-align:center;color:var(--muted);padding:3px 0;border-radius:6px}
.day b{display:block;font-size:12px;font-weight:500}
.day small{font-size:7px}
.day--active{border:2px solid var(--tab);color:var(--ink)}
.screen--calendar .tabbar{height:76px;background:#f7fbfd;color:var(--ink)}

/* copy */
.headline{position:absolute;left:48px;top:838px;color:var(--brand);line-height:.98}
.headline__strong{font-size:82px;font-weight:900;letter-spacing:-1px;display:block}
.headline__light{font-size:82px;font-weight:300;display:block}
.intro{position:absolute;left:49px;top:1030px;width:560px;font-size:21px;font-weight:300;line-height:39px;color:var(--muted)}
</style>
</head>
<body>

<!-- Daily outlook -->
<section class="screen screen--outlook" aria-label="Daily outlook screen">
  <div class="status"><span>9:41</span><span class="status__signal"><i style="height:4px"></i><i style="height:6px"></i><i style="height:8px"></i><i style="height:10px"></i></span></div>
  <div class="topbar">
    <svg width="18" height="14" viewBox="0 0 18 14"><path d="M0 1h18M0 7h18M0 13h18" stroke="#2b2f36" stroke-width="2"/></svg>
    <span class="topbar__title">DAILY OUTLOOK</span>
    <span class="topbar__actions">
      <svg width="14" height="14" viewBox="0 0 14 14"><circle cx="7" cy="7" r="6" fill="none" stroke="#2b2f36"/><path d="M7 4v6M4 7h6" stroke="#2b2f36"/></svg>
      <svg width="11" height="14" viewBox="0 0 11 14"><path d="M5.5 14S0 8 0 5.5a5.5 5.5 0 0111 0C11 8 5.5 14 5.5 14z" fill="#2b2f36"/><circle cx="5.5" cy="5.5" r="2" fill="#fff"/></svg>
    </span>
  </div>
  <div class="spots">
    <article class="spot">
      <div class="spot__photo" role="img" aria-label="Landscape photo of Rottingdean"></div>
      <div class="spot__info"><div class="spot__name">Rottingdean</div><div class="chips"><span class="chip chip--live">Live</span><span class="chip chip--good">Good</span></div><div class="spot__dist">82Km ♥</div></div>
      <span class="chart__label">Hours</span>
      <div class="chart">
        <div class="chart__col"><span class="bar" style="height:6px"></span><span class="chart__hour">08</span></div>
        <div class="chart__col"><span class="bar" style="height:8px"></span><span class="chart__hour">09</span></div>
        <div class="chart__col"><span class="bar" style="height:10px"></span><span class="chart__hour">10</span></div>
        <div class="chart__col"><span class="bar bar--y" style="height:18px"></span><span class="chart__hour">11</span></div>
        <div class="chart__col"><span class="bar bar--y" style="height:20px"></span><span class="chart__hour">12</span></div>
        <div class="chart__col"><span class="bar bar--g" style="height:24px"></span><span class="chart__hour">13</span></div>
        <div class="chart__col"><span class="bar" style="height:26px"></span><span class="chart__hour">14</span></div>
        <div class="chart__col"><span class="bar bar--g" style="height:30px"></span><span class="chart__hour">15</span></div>
      </div>
    </article>
    <article class="spot">
      <div class="spot__photo" role="img" aria-label="Landscape photo of Rye"></div>
      <div class="spot__info"><div class="spot__name">Rye</div><div class="chips"><span class="chip chip--live">Live</span><span class="chip chip--good">Good</span></div><div class="spot__dist">99Km ♥</div></div>
      <div class="chart">
        <div class="chart__col"><span class="bar" style="height:6px"></span><span class="chart__hour">08</span></div>
        <div class="chart__col"><span class="bar bar--g" style="height:14px"></span><span class="chart__hour">09</span></div>
        <div class="chart__col"><span class="bar" style="height:10px"></span><span class="chart__hour">10</span></div>
        <div class="chart__col"><span class="bar bar--y" style="height:18px"></span><span class="chart__hour">11</span></div>
        <div class="chart__col"><span class="bar bar--y" style="height:22px"></span><span class="chart__hour">12</span></div>
        <div class="chart__col"><span class="bar" style="height:26px"></span><span class="chart__hour">13</span></div>
        <div class="chart__col"><span class="bar bar--r" style="height:22px"></span><span class="chart__hour">14</span></div>
        <div class="chart__col"><span class="bar" style="height:30px"></span><span class="chart__hour">15</span></div>
      </div>
    </article>
    <article class="spot">
      <div class="spot__photo" role="img" aria-label="Landscape photo of Writtle Sports Ground"></div>
      <div class="spot__info"><div class="spot__name">Writtle Sports Ground</div><div class="chips"><span class="chip chip--live">Live</span><span class="chip chip--light">Light</span></div><div class="spot__dist">52Km ♡</div></div>
      <div class="chart">
        <div class="chart__col"><span class="bar" style="height:6px"></span><span class="chart__hour">08</span></div>
        <div class="chart__col"><span class="bar" style="height:6px"></span><span class="chart__hour">09</span></div>
        <div class="chart__col"><span class="bar" style="height:8px"></span><span class="chart__hour">10</span></div>
        <div class="chart__col"><span class="bar bar--g" style="height:14px"></span><span class="chart__hour">11</span></div>
        <div class="chart__col"><span class="bar bar--y" style="height:18px"></span><span class="chart__hour">12</span></div>
        <div class="chart__col"><span class="bar bar--r" style="height:28px"></span><span class="chart__hour">13</span></div>
        <div class="chart__col"><span class="bar bar--g" style="height:20px"></span><span class="chart__hour">14</span></div>
        <div class="chart__col"><span class="bar" style="height:24px"></span><span class="chart__hour">15</span></div>
      </div>
    </article>
    <article class="spot">
      <div class="spot__photo" role="img" aria-label="Landscape photo of Shoreham Beach"></div>
      <div class="spot__info"><div class="spot__name">Shoreham Beach</div><div class="chips"><span class="chip chip--live">Live</span><span class="chip chip--strong">Strong</span></div><div class="spot__dist">79Km ♡</div></div>
      <div class="chart">
        <div class="chart__col"><span class="bar" style="height:6px"></span><span class="chart__hour">08</span></div>
        <div class="chart__col"><span class="bar bar--g" style="height:12px"></span><span class="chart__hour">09</span></div>
        <div class="chart__col"><span class="bar" style="height:10px"></span><span class="chart__hour">10</span></div>
        <div class="chart__col"><span class="bar bar--y" style="height:14px"></span><span class="chart__hour">11</span></div>
        <div class="chart__col"><span class="bar" style="height:16px"></span><span class="chart__hour">12</span></div>
        <div class="chart__col"><span class="bar bar--g" style="height:32px"></span><span class="chart__hour">13</span></div>
        <div class="chart__col"><span class="bar" style="height:22px"></span><span class="chart__hour">14</span></div>
        <div class="chart__col"><span class="bar bar--r" style="height:20px"></span><span class="chart__hour">15</span></div>
      </div>
    </article>
    <article class="spot">
      <div class="spot__photo" role="img" aria-label="Landscape photo of Lancing Beach" style="background:linear-gradient(180deg,#6f8a6a,#a9b8b0 60%,#eef4f7)"></div>
      <div class="spot__info"><div class="spot__name">Lancing Beach</div><div class="chips"><span class="chip chip--live">Live</span><span class="chip chip--bad">Bad</span></div><div class="spot__dist">81Km ♡</div></div>
      <div class="chart">
        <div class="chart__col"><span class="bar" style="height:6px"></span></div>
        <div class="chart__col"><span class="bar bar--g" style="height:8px"></span></div>
        <div class="chart__col"><span class="bar" style="height:10px"></span></div>
        <div class="chart__col"><span class="bar bar--y" style="height:16px"></span></div>
        <div class="chart__col"><span class="bar bar--r" style="height:22px"></span></div>
        <div class="chart__col"><span class="bar" style="height:24px"></span></div>
        <div class="chart__col"><span class="bar" style="height:26px"></span></div>
        <div class="chart__col"><span class="bar" style="height:28px"></span></div>
      </div>
    </article>
  </div>
  <nav class="tabbar">
    <span class="tabbar__item"><svg width="14" height="14" viewBox="0 0 14 14"><circle cx="6" cy="6" r="4.5" fill="none" stroke="#2b2f36" stroke-width="1.5"/><path d="M9.5 9.5L13 13" stroke="#2b2f36" stroke-width="1.5"/></svg>Explore</span>
    <span class="tabbar__calendar"><svg width="18" height="18" viewBox="0 0 18 18"><rect x="1" y="3" width="16" height="14" rx="2" fill="none" stroke="#2b5f7a" stroke-width="1.5"/><path d="M1 7h16M5 1v4M13 1v4" stroke="#2b5f7a" stroke-width="1.5"/></svg></span>
    <span class="tabbar__item"><svg width="14" height="13" viewBox="0 0 14 13"><path d="M7 12S1 8 1 4.2A3 3 0 017 3a3 3 0 016 1.2C13 8 7 12 7 12z" fill="none" stroke="#2b2f36" stroke-width="1.3"/></svg>Favorites</span>
  </nav>
</section>

<!-- Detailed forecast -->
<section class="screen screen--detail" aria-label="Detailed hourly forecast screen">
  <div class="detail__hero" role="img" aria-label="Sky and sea photo behind the spot header"></div>
  <div class="detail__head">
    <div class="status"><span>9:41</span><span class="status__signal"><i style="height:4px"></i><i style="height:6px"></i><i style="height:8px"></i><i style="height:10px"></i></span></div>
    <div class="topbar">
      <svg width="16" height="12" viewBox="0 0 16 12"><path d="M16 6H2M6 1L1 6l5 5" fill="none" stroke="#1f3a40" stroke-width="1.5"/></svg>
      <span class="detail__location">BRACKLESHAM</span>
      <span class="follow">Follow</span>
      <span class="topbar__actions"><span class="avatar"></span></span>
    </div>
  </div>
  <div class="detail__spot">
    <div class="detail__spotname">Rottingdean <span class="chip chip--live">Live</span></div>
    <div class="detail__stats">
      <span class="detail__temp">8°C</span>
      <span class="stat"><b>1.6m</b><span>Tide</span></span>
      <span class="stat"><b>0</b><span>Kts</span></span>
      <span class="stat"><b>-</b><span>m²</span></span>
    </div>
    <div class="detail__sub">Thursday 21 hourly forecast</div>
  </div>
  <div class="hourly">
    <div class="hour">
      <span class="hour__time"><b>08:00</b><small>am</small><br><span class="chip chip--good">Good</span></span>
      <svg width="18" height="12" viewBox="0 0 18 12"><path d="M4 11h10a3 3 0 000-6 5 5 0 00-9.5 1A2.5 2.5 0 004 11z" fill="none" stroke="#fff"/></svg>
      <span class="cell">10°C<small>Temp</small></span>
      <span class="cell"><svg width="9" height="9" viewBox="0 0 9 9"><path d="M4.5 0L9 9 4.5 7 0 9z" fill="#fff"/></svg><small>Wind</small></span>
      <span class="cell">09<small>Kts</small></span>
      <span class="cell">0.3<small>m</small></span>
      <span class="warn">21</span>
    </div>
    <div class="hour">
      <span class="hour__time"><b>10:00</b><small>am</small><br><span class="chip chip--good">Good</span></span>
      <svg width="18" height="12" viewBox="0 0 18 12"><path d="M4 11h10a3 3 0 000-6 5 5 0 00-9.5 1A2.5 2.5 0 004 11z" fill="none" stroke="#fff"/></svg>
      <span class="cell">11°C</span>
      <span class="cell"><svg width="9" height="9" viewBox="0 0 9 9"><path d="M4.5 0L9 9 4.5 7 0 9z" fill="#fff"/></svg></span>
      <span class="cell">09</span>
      <span class="cell">12.6</span>
      <span class="warn">20</span>
    </div>
    <div class="hour">
      <span class="hour__time"><b>11:00</b><small>am</small><br><span class="chip chip--bad">Bad</span></span>
      <svg width="18" height="14" viewBox="0 0 18 14"><path d="M4 9h10a3 3 0 000-6 5 5 0 00-9.5 1A2.5 2.5 0 004 9zM6 11l-1 2M10 11l-1 2" fill="none" stroke="#fff"/></svg>
      <span class="cell">10°C</span>
      <span class="cell"><svg width="9" height="9" viewBox="0 0 9 9"><path d="M4.5 0L9 9 4.5 7 0 9z" fill="#fff"/></svg></span>
      <span class="cell">09</span>
      <span class="cell">-1.0m</span>
      <span class="warn">19</span>
    </div>
    <div class="hour">
      <span class="hour__time"><b>12:00</b><small>pm</small><br><span class="chip chip--strong">Strong</span></span>
      <svg width="18" height="12" viewBox="0 0 18 12"><path d="M4 11h10a3 3 0 000-6 5 5 0 00-9.5 1A2.5 2.5 0 004 11z" fill="none" stroke="#fff"/></svg>
      <span class="cell">10°C</span>
      <span class="cell"><svg width="9" height="9" viewBox="0 0 9 9"><path d="M4.5 0L9 9 4.5 7 0 9z" fill="#fff"/></svg></span>
      <span class="cell">09</span>
      <span class="cell">-</span>
      <span class="cell">17</span>
    </div>
  </div>
  <nav class="tabbar tabbar--clear">
    <span class="tabbar__item"><svg width="14" height="14" viewBox="0 0 14 14"><circle cx="6" cy="6" r="4.5" fill="none" stroke="#fff" stroke-width="1.5"/><path d="M9.5 9.5L13 13" stroke="#fff" stroke-width="1.5"/></svg>Explore</span>
    <span class="tabbar__calendar"><svg width="18" height="18" viewBox="0 0 18 18"><rect x="1" y="3" width="16" height="14" rx="2" fill="none" stroke="#2b5f7a" stroke-width="1.5"/><path d="M1 7h16M5 1v4M13 1v4" stroke="#2b5f7a" stroke-width="1.5"/></svg></span>
    <span class="tabbar__item"><svg width="14" height="13" viewBox="0 0 14 13"><path d="M7 12S1 8 1 4.2A3 3 0 017 3a3 3 0 016 1.2C13 8 7 12 7 12z" fill="none" stroke="#fff" stroke-width="1.3"/></svg>Favorites</span>
  </nav>
</section>

<!-- Date picker -->
<section class="screen screen--calendar" aria-label="Daily outlook with date picker">
  <div class="topbar" style="padding-top:44px;color:#11181c">
    <svg width="22" height="14" viewBox="0 0 22 14"><path d="M0 1h22M0 7h22M0 13h18" stroke="#11181c" stroke-width="2"/></svg>
    <span class="topbar__title">DAILY OUTLOOK</span>
    <span class="topbar__actions">
      <svg width="16" height="16" viewBox="0 0 16 16"><circle cx="8" cy="8" r="7" fill="none" stroke="#11181c" stroke-width="1.5"/><path d="M8 4v8M4 8h8" stroke="#11181c" stroke-width="1.5"/></svg>
      <svg width="11" height="14" viewBox="0 0 11 14"><path d="M5.5 14S0 8 0 5.5a5.5 5.5 0 0111 0C11 8 5.5 14 5.5 14z" fill="#11181c"/></svg>
    </span>
  </div>
  <div class="calendar__list">
    <div class="ghost"><div class="chart"><span class="bar" style="height:6px"></span><span class="bar" style="height:8px"></span><span class="bar bar--y" style="height:20px"></span><span class="bar bar--y" style="height:24px"></span><span class="bar bar--g" style="height:22px"></span><span class="bar" style="height:26px"></span><span class="bar bar--g" style="height:28px"></span></div></div>
    <div class="ghost"><div class="chart"><span class="bar" style="height:6px"></span><span class="bar" style="height:8px"></span><span class="bar bar--y" style="height:22px"></span><span class="bar bar--y" style="height:26px"></span><span class="bar bar--r" style="height:24px"></span><span class="bar" style="height:26px"></span><span class="bar" style="height:28px"></span></div></div>
    <div class="ghost"><div class="chart"><span class="bar" style="height:6px"></span><span class="bar" style="height:8px"></span><span class="bar bar--y" style="height:18px"></span><span class="bar bar--g" style="height:22px"></span><span class="bar bar--r" style="height:26px"></span><span class="bar" style="height:24px"></span><span class="bar bar--g" style="height:22px"></span></div></div>
  </div>
  <div class="picker">
    <div class="picker__head"><span>January ⌄</span><span>2018 ⌄</span></div>
    <div class="picker__days">
      <span class="day"><b>18</b><small>Sun</small></span>
      <span class="day"><b>19</b><small>Mon</small></span>
      <span class="day"><b>20</b><small>Tue</small></span>
      <span class="day day--active"><b>21</b><small>Wed</small></span>
      <span class="day"><b>🔒︎</b><small>Thu</small></span>
      <span class="day"><b>🔒︎</b><small>Fri</small></span>
      <span class="day"><b>🔒︎</b><small>Sat</small></span>
    </div>
  </div>
  <nav class="tabbar">
    <span class="tabbar__item"><svg width="16" height="16" viewBox="0 0 14 14"><circle cx="6" cy="6" r="4.5" fill="none" stroke="#2b2f36" stroke-width="1.5"/><path d="M9.5 9.5L13 13" stroke="#2b2f36" stroke-width="1.5"/></svg>Explore</span>
    <span class="tabbar__calendar" style="height:66px"><svg width="18" height="18" viewBox="0 0 18 18"><rect x="1" y="3" width="16" height="14" rx="2" fill="none" stroke="#2b5f7a" stroke-width="1.5"/><path d="M1 7h16M5 1v4M13 1v4" stroke="#2b5f7a" stroke-width="1.5"/></svg></span>
    <span class="tabbar__item"><svg width="16" height="15" viewBox="0 0 14 13"><path d="M7 12S1 8 1 4.2A3 3 0 017 3a3 3 0 016 1.2C13 8 7 12 7 12z" fill="none" stroke="#2b2f36" stroke-width="1.3"/></svg>Favorites</span>
  </nav>
</section>

<h1 class="headline"><span class="headline__strong">KiteSurf</span><span class="headline__light">Weather App</span></h1>
<p class="intro">BreezeLedger. Our main screen is the forecast screen. The forecast screen presents the forecast for multiple places for the selected day.</p>

</body>
</html>
```